Business Broker Website

This website will be for a business broker. The logo is attached and will need to be in the footer as it is but in the header please remove the word 'group' and replace with 'business sales' (so that it is morvale business sales).
It needs to be a modern high end corporate font for the logo and also for the rest of the site. Please only use fonts available on fonts.google.com
It needs to have 4 prominent boxes at the top of the page that say 'business listings', 'appraisal report', 'what we do' and 'who we are'
The 'what we do' section needs to have sub menu items for 'sectors' and 'services'. The who we are section needs to have sub menu items for 'about us' and 'team'
The top menu needs to have :
* Home
* Businesses for Sale
* Sell your Business
* What we do
* About Us
* Contact
This needs to be seen as the #1 business broker in Australia. It needs to attract serious high quality buyers and sellers and needs to be highly professional, premium and straight to the point and innovative.
It needs to show that Morvale Business Sales not only do SME sales but also do Corporate Mergers and Acquisitions.
They like the look of the site at https://brackenhurstadvisors.com/en-us/
They also love the look of https://quarlingcapital.com/ (they prefer this to the above site)
The website features a clean, minimalist layout with ample white space, making it easy to navigate and visually appealing. The typography is modern and legible, and the color palette is professional, enhancing the site's overall aesthetic. High-quality images and a responsive design contribute to its polished appearance.
Please note this is for an Australian based business.
Contact details to show in the footer:
Head Office
Suite 17, Second Floor
48 Tarrant Street
Oakmere Vale
VIC 3842
1300 62 19 05
info@morvalegroup.com.au
If you need some wording for the site, look at https://www.morvalegroup.com.au/businesssales which is a page about their business division. Don't use all this content though as they want it straight to the point and not rambling on.

```html
<!DOCTYPE html>
<html lang="en">
<head>
<meta charset="utf-8">
<title>Morvale Business Sales</title>
<link href="https://fonts.googleapis.com/css2?family=Inter:wght@400;500;600&family=Playfair+Display:wght@600;700&display=swap" rel="stylesheet">
<style>
  :root {
    --orange: #e05226;
    --ink: #1f2026;
    --text: #2b2b2f;
    --muted: #55565c;
    --page: #f6f6f6;
    --white: #ffffff;
    --footer: #20222a;
    --footer-text: #c9cacf;
    --footer-dim: #9b9ca3;
    --menu-blue: #2a4a8a;
  }
  * { margin: 0; padding: 0; box-sizing: border-box; }
  html, body { width: 794px; height: 1200px; overflow: hidden; }
  body { position: relative; background: var(--page); font-family: "Inter", sans-serif; color: var(--text); }

  /* Header */
  .site-header { position: absolute; left: 0; top: 0; width: 794px; height: 62px; background: var(--page); }
  .brand { position: absolute; left: 59px; top: 24px; display: flex; align-items: center; gap: 6px; }
  .brand-mark { width: 12px; height: 12px; border-radius: 50%; background: var(--orange); flex: none; }
  .brand-name { font-weight: 600; font-size: 13px; color: var(--ink); letter-spacing: -0.2px; white-space: nowrap; }
  .main-nav { position: absolute; right: 58px; top: 22px; height: 29px; display: flex; align-items: center; gap: 12px; }
  .nav-item { font-size: 10px; font-weight: 500; color: var(--ink); white-space: nowrap; display: flex; align-items: center; justify-content: center; gap: 6px; height: 29px; }
  .nav-item.has-menu { background: var(--white); padding: 0 10px; }
  .nav-item svg { width: 10px; height: 6px; }

  /* Hero */
  .hero { position: absolute; left: 0; top: 62px; width: 794px; height: 384px; overflow: hidden; }
  .hero-bg { position: absolute; inset: 0; background: linear-gradient(180deg, #2f3136 0%, #26272b 45%, #3a342f 80%, #2a2826 100%); }
  .hero-shade { position: absolute; inset: 0; background: radial-gradient(ellipse at 50% 30%, rgba(20,20,24,0.55), rgba(20,20,24,0.15) 70%); }
  .hero-title { position: absolute; left: 0; width: 794px; text-align: center; font-family: "Playfair Display", serif; font-weight: 700; font-size: 34px; line-height: 32px; color: var(--white); top: 26px; }
  .hero-title .accent { color: var(--orange); display: block; }
  .hero-sub { position: absolute; left: 0; width: 794px; top: 96px; text-align: center; color: var(--white); font-size: 11.5px; line-height: 16.5px; font-weight: 500; }

  .entry-card { position: absolute; top: 148px; width: 127px; height: 163px; background: var(--white); text-align: center; }
  .entry-icon { width: 31px; height: 31px; margin: 17px auto 0; display: flex; align-items: center; justify-content: center; }
  .entry-icon.orange { background: var(--orange); }
  .entry-icon.dark { background: var(--ink); }
  .entry-icon svg { width: 17px; height: 17px; }
  .entry-title { font-family: "Playfair Display", serif; font-weight: 600; font-size: 10px; color: var(--ink); margin-top: 8px; }
  .entry-text { font-size: 8px; line-height: 13.2px; color: var(--text); margin-top: 7px; }
  .entry-link { position: absolute; left: 0; right: 0; top: 134px; font-size: 7px; font-weight: 600; color: var(--orange); }
  .hero-cta { position: absolute; left: 323px; top: 336px; width: 147px; height: 23px; background: var(--orange); color: var(--white); font-size: 8.7px; font-weight: 600; display: flex; align-items: center; justify-content: center; }

  /* Why section */
  .why-heading { position: absolute; left: 0; width: 794px; top: 490px; text-align: center; font-family: "Playfair Display", serif; font-weight: 700; font-size: 23px; color: var(--ink); }
  .why-intro { position: absolute; left: 0; width: 794px; top: 528px; text-align: center; font-size: 9.5px; line-height: 14px; color: var(--muted); font-weight: 500; }
  .feature-card { position: absolute; top: 590px; width: 206px; height: 129px; background: var(--white); text-align: center; }
  .feature-icon { width: 31px; height: 31px; border-radius: 50%; margin: 16px auto 0; display: flex; align-items: center; justify-content: center; }
  .feature-icon.warm { background: #f6e4de; }
  .feature-icon.cool { background: #ececec; }
  .feature-icon svg { width: 15px; height: 15px; }
  .feature-title { font-family: "Playfair Display", serif; font-weight: 600; font-size: 10.5px; color: var(--ink); margin-top: 9px; }
  .feature-text { font-size: 8px; line-height: 12.3px; color: var(--text); margin-top: 8px; padding: 0 16px; }

  /* Call to action */
  .cta-panel { position: absolute; left: 215px; top: 753px; width: 363px; height: 151px; background: var(--orange); text-align: center; color: var(--white); }
  .cta-title { font-family: "Playfair Display", serif; font-weight: 600; font-size: 13px; margin-top: 24px; }
  .cta-text { font-size: 9px; line-height: 14px; margin-top: 9px; }
  .cta-actions { position: absolute; top: 104px; left: 0; width: 363px; }
  .btn { position: absolute; top: 0; height: 23px; font-size: 8px; font-weight: 500; display: flex; align-items: center; justify-content: center; }
  .btn-solid { left: 70px; width: 118px; background: var(--white); color: var(--orange); }
  .btn-outline { left: 197px; width: 96px; border: 1px solid var(--white); color: var(--white); }

  /* Footer */
  .site-footer { position: absolute; left: 0; top: 955px; width: 794px; height: 245px; background: var(--footer); color: var(--footer-text); }
  .footer-brand { position: absolute; left: 72px; top: 34px; display: flex; align-items: center; gap: 6px; }
  .footer-brand .brand-name { color: var(--white); font-size: 15px; }
  .footer-about { position: absolute; left: 72px; top: 73px; width: 240px; font-size: 8.2px; line-height: 12.3px; }
  .footer-label { position: absolute; left: 72px; top: 130px; font-size: 8.5px; font-weight: 600; color: var(--white); }
  .footer-accred { position: absolute; left: 72px; top: 146px; font-size: 7.3px; color: var(--footer-dim); }
  .footer-col { position: absolute; top: 34px; }
  .footer-col h4 { font-family: "Playfair Display", serif; font-weight: 600; font-size: 9px; color: var(--white); }
  .service-list { list-style: none; margin-top: 15px; font-size: 8.5px; }
  .service-list li { height: 17.8px; }
  .office dt { font-size: 7.3px; font-weight: 600; color: var(--white); margin-top: 8px; }
  .office dt:first-child { margin-top: 15px; }
  .office dd { font-size: 6.6px; line-height: 9.9px; }
  .footer-rule { position: absolute; left: 73px; top: 192px; width: 648px; height: 1px; background: #3c3e46; }
  .footer-copy { position: absolute; left: 72px; top: 206px; font-size: 6.8px; color: var(--footer-dim); }
  .legal-links { position: absolute; right: 73px; top: 206px; display: flex; gap: 12px; font-size: 6.8px; color: var(--footer-dim); }
</style>
</head>
<body>

<header class="site-header">
  <div class="brand">
    <span class="brand-mark"></span>
    <span class="brand-name">Morvale Business Sales</span>
  </div>
  <nav class="main-nav">
    <span class="nav-item">Home</span>
    <span class="nav-item">Business For Sale</span>
    <span class="nav-item">Sell Your Business</span>
    <span class="nav-item has-menu">What We Do
      <svg viewBox="0 0 10 6"><path d="M1 1l4 4 4-4" fill="none" stroke="#1f2026" stroke-width="1.2"/></svg></span>
    <span class="nav-item has-menu">About Us
      <svg viewBox="0 0 10 6"><path d="M1 1l4 4 4-4" fill="none" stroke="#2a4a8a" stroke-width="1.2"/></svg></span>
    <span class="nav-item">Contact</span>
  </nav>
</header>

<section class="hero">
  <div class="hero-bg" role="img" aria-label="Evening view of glass office towers and a city street"></div>
  <div class="hero-shade"></div>
  <h1 class="hero-title">Australia’s Premier<span class="accent">Business Brokers</span></h1>
  <p class="hero-sub">Specializing in SME sales and corporate M&amp;A transactions.<br>Expert valuations, strategic advisory, and seamless business transfers.</p>

  <div class="entry-card" style="left:127px;">
    <div class="entry-icon orange"><svg viewBox="0 0 24 24" fill="none" stroke="#fff" stroke-width="1.6"><rect x="5" y="3" width="14" height="18" rx="2"/><path d="M8.5 8h7M8.5 11h7M8.5 14h7M8.5 17h4"/></svg></div>
    <h2 class="entry-title">Business Listings</h2>
    <p class="entry-text">Browse our exclusive<br>portfolio of premium<br>businesses for sale<br>across Australia</p>
    <span class="entry-link">View Listings →</span>
  </div>
  <div class="entry-card" style="left:265px;">
    <div class="entry-icon dark"><svg viewBox="0 0 24 24" fill="none" stroke="#fff" stroke-width="1.6"><path d="M6 3h8l4 4v14H6z"/><path d="M9.5 17v-2M12 17v-4M14.5 17v-6"/></svg></div>
    <h2 class="entry-title">Appraisal Report</h2>
    <p class="entry-text">Get a comprehensive<br>business valuation<br>from our certified<br>professionals</p>
    <span class="entry-link">Get Appraisal →</span>
  </div>
  <div class="entry-card" style="left:402px;">
    <div class="entry-icon orange"><svg viewBox="0 0 24 24" fill="none" stroke="#fff" stroke-width="1.6"><path d="M4 4v16h16"/><path d="M7 16l4-5 3 3 5-6"/></svg></div>
    <h2 class="entry-title">What We Do</h2>
    <p class="entry-text">Discover our<br>comprehensive business<br>brokerage and<br>M&amp;A services</p>
    <span class="entry-link">Our Services →</span>
  </div>
  <div class="entry-card" style="left:540px;">
    <div class="entry-icon dark"><svg viewBox="0 0 24 24" fill="#fff"><circle cx="12" cy="8" r="3"/><circle cx="6" cy="9" r="2.2"/><circle cx="18" cy="9" r="2.2"/><path d="M7 19c0-3 2.2-5 5-5s5 2 5 5z"/><path d="M2 18c0-2.4 1.6-4 4-4 .8 0 1.4.2 2 .5-1 1-1.6 2.2-1.8 3.5z"/><path d="M22 18c0-2.4-1.6-4-4-4-.8 0-1.4.2-2 .5 1 1 1.6 2.2 1.8 3.5z"/></svg></div>
    <h2 class="entry-title">Who We Are</h2>
    <p class="entry-text">Meet our expert<br>team and learn<br>about our proven<br>track record</p>
    <span class="entry-link">About Us →</span>
  </div>

  <span class="hero-cta">Start Your Business Journey</span>
</section>

<h2 class="why-heading">Why Choose Morvale Business Sales?</h2>
<p class="why-intro">We are Australia’s most trusted business brokerage firm, delivering exceptional results<br>through expertise, integrity, and unwavering commitment to our clients.</p>

<div class="feature-card" style="left:77px;">
  <div class="feature-icon warm"><svg viewBox="0 0 24 24" fill="none" stroke="#e05226" stroke-width="1.6"><path d="M12 3l2.3 1.6 2.8-.2.9 2.6 2.3 1.6-.9 2.7.9 2.7-2.3 1.6-.9 2.6-2.8-.2L12 21l-2.3-1.6-2.8.2-.9-2.6L3.7 15.4l.9-2.7-.9-2.7L6 8.4 6.9 5.8l2.8.2z"/><path d="M9 12l2 2 4-4"/></svg></div>
  <h3 class="feature-title">Proven Track Record</h3>
  <p class="feature-text">Over 15 years of successful business<br>transactions, from SME sales to complex<br>corporate M&amp;A deals.</p>
</div>
<div class="feature-card" style="left:294px;">
  <div class="feature-icon cool"><svg viewBox="0 0 24 24" fill="none" stroke="#1f2026" stroke-width="1.6"><path d="M13 2L5 14h6l-1 8 8-12h-6z"/></svg></div>
  <h3 class="feature-title">Expert Team</h3>
  <p class="feature-text">Licensed professionals with deep industry<br>knowledge and strategic expertise across all<br>business sectors.</p>
</div>
<div class="feature-card" style="left:511px;">
  <div class="feature-icon warm"><svg viewBox="0 0 24 24" fill="none" stroke="#e05226" stroke-width="1.6"><rect x="5" y="10" width="14" height="11" rx="1.5"/><path d="M8 10V7a4 4 0 018 0v3M12 14v3"/></svg></div>
  <h3 class="feature-title">Confidential Process</h3>
  <p class="feature-text">Strict confidentiality protocols<br>ensure your business sale or acquisition<br>remains completely private.</p>
</div>

<section class="cta-panel">
  <h2 class="cta-title">Ready to Make Your Next Move?</h2>
  <p class="cta-text">Whether you’re looking to buy, sell, or grow your business, our team is ready<br>to guide you through every step of the process with professional expertise<br>and personalized service.</p>
  <div class="cta-actions">
    <span class="btn btn-solid">Schedule a Consultation</span>
    <span class="btn btn-outline">Call 1300 62 19 05</span>
  </div>
</section>

<footer class="site-footer">
  <div class="footer-brand">
    <span class="brand-mark"></span>
    <span class="brand-name">Morvale Group</span>
  </div>
  <p class="footer-about">Australia’s premier business brokerage firm specializing in<br>SME sales and corporate M&amp;A transactions.<br>We deliver exceptional outcomes for serious buyers<br>and sellers across all industry sectors.</p>
  <p class="footer-label">Professional Accreditations</p>
  <p class="footer-accred">Licensed Business Brokers | M&amp;A Advisory Specialists | NBBA Members</p>

  <div class="footer-col" style="left:404px;">
    <h4>Services</h4>
    <ul class="service-list">
      <li>Business Sales</li>
      <li>Business Valuations</li>
      <li>M&amp;A Advisory</li>
      <li>Due Diligence</li>
      <li>Strategic Planning</li>
    </ul>
  </div>
  <div class="footer-col" style="left:570px;">
    <h4>Head Office</h4>
    <dl class="office">
      <dt>Address</dt>
      <dd>Suite 17, Second Floor<br>48 Tarrant Street<br>Oakmere Vale<br>VIC 3842</dd>
      <dt>Phone</dt>
      <dd>1300 62 19 05</dd>
      <dt>Email</dt>
      <dd>info@morvalegroup.com.au</dd>
    </dl>
  </div>

  <div class="footer-rule"></div>
  <p class="footer-copy">© 2024 Morvale Business Sales. All rights reserved.</p>
  <div class="legal-links"><span>Privacy Policy</span><span>Terms of Service</span><span>Disclaimer</span></div>
</footer>

</body>
</html>
```